Design a Logo and business card

I need a logo and business card for Marovinta.
Business card must suit logo and be neat and modern.
Business card must be back and front. It must also contain dummy data that I can edit in either photoshop or illustrator.

```html
<!DOCTYPE html>
<html lang="en">
<head>
<meta charset="utf-8">
<title>Marovinta — Business Card</title>
<link href="https://fonts.googleapis.com/css2?family=Jura:wght@400;500&display=swap" rel="stylesheet">
<style>
  :root {
    --backdrop: #ebebeb;
    --card-paper: #f4f3ef;
    --brand-blue: #1f9fd8;
    --brand-green: #7ab236;
  }
  * { margin: 0; padding: 0; box-sizing: border-box; }
  html, body {
    width: 1200px;
    height: 900px;
    overflow: hidden;
    background: var(--backdrop);
    font-family: "Jura", sans-serif;
  }
  .business-card {
    position: absolute;
    left: 60px;
    top: 134px;
    width: 1080px;
    height: 632px;
    background: var(--card-paper);
  }
  .holder-name {
    position: absolute;
    left: 68px;
    top: 112px;
    font-size: 64px;
    font-weight: 500;
    letter-spacing: 1px;
    color: var(--brand-blue);
    line-height: 1;
    white-space: nowrap;
  }
  .holder-role {
    position: absolute;
    left: 68px;
    top: 196px;
    font-size: 32px;
    letter-spacing: 2px;
    color: var(--brand-blue);
    line-height: 1;
  }
  .contact-list {
    position: absolute;
    left: 68px;
    top: 284px;
    list-style: none;
    font-size: 29px;
    font-weight: 500;
    letter-spacing: 1px;
    color: var(--brand-green);
    line-height: 40px;
  }
  .contact-list .group-gap { margin-top: 47px; }
  .contact-label { display: inline-block; width: 36px; }
  .brand-lockup {
    position: absolute;
    right: 38px;
    top: 330px;
    display: flex;
    align-items: center;
    gap: 16px;
  }
  .brand-square {
    width: 34px;
    height: 34px;
    background: var(--brand-green);
  }
  .brand-name {
    font-size: 56px;
    font-weight: 500;
    color: var(--brand-blue);
    line-height: 1;
  }
  .footer-bands {
    position: absolute;
    left: 0;
    top: 586px;
    width: 1080px;
    height: 44px;
  }
</style>
</head>
<body>
  <section class="business-card" aria-label="Business card front">
    <h1 class="holder-name">Dario Velkovski</h1>
    <p class="holder-role">seo &amp; web designer</p>

    <ul class="contact-list">
      <li><span class="contact-label">T:</span> +381 21 4820 316</li>
      <li><span class="contact-label">M:</span> +381 63 502 7188</li>
      <li class="group-gap"><span class="contact-label">E:</span> dario.velkovski@marovinta.com</li>
      <li><span class="contact-label">W:</span> velkostudio.com</li>
    </ul>

    <div class="brand-lockup">
      <span class="brand-square" aria-hidden="true"></span>
      <span class="brand-name">Marovinta</span>
    </div>

    <svg class="footer-bands" viewBox="0 0 1080 44" aria-hidden="true">
      <rect x="0" y="0" width="702" height="44" fill="var(--brand-green)"/>
      <rect x="717" y="0" width="363" height="44" fill="var(--brand-blue)"/>
    </svg>
  </section>
</body>
</html>
```